Tarnwickhub.com home page

On the existing home page I want to eliminate people in circles and promote these three earning opportunities:
1." Make a referral to existing advertiser"
Earn up to $5000 when you make a successful referral to one of our advertisers.
2."Sign up a new business to offer referral commisions to ambassaadors". Earn up to $5000 or more when you earn 5% of money paid out by business in referral fees.
3."Sign up new ambassadors"
Earn up to $5000 or more when you earn 5% of the money the ambassadors you sign up earn.

In each offer I want a learn more button .

Industry/Entity Type

Business

Font styles to use
Serif

```html
<!DOCTYPE html>
<html lang="en">
<head>
<meta charset="utf-8">
<title>Tarnwickhub.com – Referral Marketplace</title>
<link rel="stylesheet" href="https://fonts.googleapis.com/css2?family=Roboto:wght@400;500;700;900&family=Open+Sans:ital,wght@0,400;0,600;0,700;1,400;1,600;1,700&display=swap">
<style>
  :root {
    --green: #27a24a;
    --green-dark: #138a36;
    --green-bright: #3cbc54;
    --lime: #8cc421;
    --lime-dark: #79b316;
    --ink: #1d1d1d;
    --ink-soft: #3a3a3a;
    --navy: #1a3a6b;
    --nav-ink: #5c5c5c;
    --page: #f4f5f7;
    --card: #fbfbfc;
    --line: #e2e4e7;
  }
  * { box-sizing: border-box; margin: 0; padding: 0; }
  html, body { width: 1200px; height: 786px; overflow: hidden; }
  body {
    position: relative;
    background: linear-gradient(#ffffff 64px, #f6f7f9 200px, var(--page) 660px);
    font-family: "Open Sans", Arial, sans-serif;
    color: var(--ink);
  }

  .site-header {
    position: absolute; left: 0; top: 0; width: 1200px; height: 64px;
    background: #fff; border-bottom: 1px solid #ececec;
  }
  .brand {
    position: absolute; left: 136px; top: 12px;
    font-family: "Roboto", Arial, sans-serif; font-weight: 700;
    font-size: 32px; color: var(--green); letter-spacing: -0.5px;
  }
  .main-nav { position: absolute; left: 722px; top: 0; display: flex; height: 64px; }
  .main-nav a {
    display: flex; align-items: center; height: 64px; padding: 0 14px;
    font-family: "Roboto", Arial, sans-serif; font-size: 14px;
    color: var(--nav-ink); text-decoration: none;
  }
  .main-nav a.is-active { background: var(--green); color: #fff; padding: 0 18px; }

  .hero-title {
    position: absolute; left: 0; top: 78px; width: 1200px; text-align: center;
    font-family: "Roboto", Arial, sans-serif; font-weight: 900;
    font-size: 36px; letter-spacing: 1.5px; color: var(--ink);
  }
  .hero-subtitle {
    position: absolute; left: 0; top: 114px; width: 1200px; text-align: center;
    font-family: "Roboto", Arial, sans-serif; font-weight: 500;
    font-size: 27px; letter-spacing: 0.3px; color: var(--ink);
  }
  .hero-note {
    position: absolute; left: 277px; top: 148px; width: 660px;
    font-size: 13.5px; line-height: 19px; color: var(--ink-soft);
  }
  .hero-note strong { color: var(--navy); }

  .offer {
    position: absolute; top: 205px; width: 244px; height: 419px;
    background: linear-gradient(var(--card), #f3f4f6);
    border: 1px solid #dcdfe3; border-radius: 14px; overflow: hidden;
    box-shadow: 0 1px 3px rgba(0,0,0,0.08);
  }
  .offer--one { left: 222px; }
  .offer--two { left: 478px; }
  .offer--three { left: 734px; }
  .offer__head { position: relative; height: 139px; }
  .offer__head svg { position: absolute; inset: 0; }
  .offer__label {
    position: absolute; left: 40px; top: 90px;
    font-family: "Roboto", Arial, sans-serif; font-weight: 500;
    font-size: 27px; color: #fff;
  }
  .offer__number {
    position: absolute; left: 112px; top: -8px;
    font-family: "Roboto", Arial, sans-serif; font-weight: 400;
    font-size: 140px; line-height: 150px; color: #fff;
  }
  .offer--two .offer__number { left: 108px; }
  .offer--three .offer__number { left: 116px; }
  .offer__title {
    position: absolute; left: 22px; top: 158px; width: 200px; text-align: center;
    font-style: italic; font-weight: 600; font-size: 16px; line-height: 19px;
    color: var(--ink-soft);
  }
  .offer__rule {
    position: absolute; left: 50px; width: 144px; height: 1px;
    background: linear-gradient(90deg, transparent, var(--line), transparent);
  }
  .offer__rule--top { top: 234px; }
  .offer__rule--bottom { top: 335px; }
  .offer__text {
    position: absolute; left: 18px; top: 258px; width: 208px; text-align: center;
    font-style: italic; font-size: 12.5px; line-height: 18px; color: var(--ink);
  }
  .offer__amount {
    font-style: italic; font-weight: 700; font-size: 17px; color: var(--green);
  }
  .offer__button {
    position: absolute; left: 49px; top: 360px; width: 146px; height: 37px;
    display: flex; align-items: center; justify-content: center;
    background: linear-gradient(#a6d23c, var(--lime-dark));
    border: 1px solid #6fa11a; border-radius: 4px;
    font-size: 13px; color: #3c4f12; text-decoration: none;
    box-shadow: inset 0 1px 0 rgba(255,255,255,0.4);
  }

  .payout-band {
    position: absolute; left: 0; top: 661px; width: 1200px; height: 59px;
    background: #fff; border-top: 1px solid #e6e7ea;
    display: flex; align-items: center; justify-content: center; gap: 14px;
  }
  .payout-band__label {
    font-family: "Roboto", Arial, sans-serif; font-size: 32px; color: var(--navy);
  }
  .payout-band__amount {
    font-family: "Roboto", Arial, sans-serif; font-weight: 700;
    font-size: 44px; color: var(--green-dark);
  }

  .signup-band {
    position: absolute; left: 0; top: 720px; width: 1200px; height: 66px;
    background: var(--green-bright);
  }
  .signup-band__text {
    position: absolute; left: 128px; top: 22px;
    font-size: 16px; font-weight: 600; color: #fff;
  }
  .signup-band__button {
    position: absolute; left: 914px; top: 13px; width: 160px; height: 40px;
    border: 2px solid #fff; border-radius: 3px;
    display: flex; align-items: center; justify-content: center; gap: 9px;
    font-size: 15px; color: #fff; text-decoration: none;
  }
</style>
</head>
<body>
  <header class="site-header">
    <div class="brand">TarnwickHub</div>
    <nav class="main-nav">
      <a class="is-active" href="#">Home</a>
      <a href="#">How It Works</a>
      <a href="#">Search</a>
      <a href="#">Members</a>
      <a href="#">Log In</a>
    </nav>
  </header>

  <h1 class="hero-title">EASILY MAKE MORE MONEY</h1>
  <h2 class="hero-subtitle">JUST BY REFERRING YOURSELF, YOUR FRIENDS OR BUSINESS ASSOCIATES</h2>
  <p class="hero-note">These <strong>Top Ambassadors</strong> increased their annual income by 50% just by referring associates about services in our network!</p>

  <section class="offer offer--one">
    <div class="offer__head">
      <svg width="244" height="139" viewBox="0 0 244 139">
        <defs>
          <linearGradient id="headGreen" x1="0" y1="0" x2="0" y2="1">
            <stop offset="0" stop-color="#1f9a3e"/><stop offset="1" stop-color="#2cb04f"/>
          </linearGradient>
        </defs>
        <rect width="244" height="139" fill="url(#headGreen)"/>
        <path d="M0 139 C30 40 130 -10 244 10 L244 139 Z" fill="#ffffff" opacity="0.08"/>
      </svg>
      <span class="offer__label">Offer</span>
      <span class="offer__number">1</span>
    </div>
    <h3 class="offer__title">Make a Referral to Existing Advertiser</h3>
    <div class="offer__rule offer__rule--top"></div>
    <p class="offer__text">Earn up to <span class="offer__amount">$5000</span> when you emake a successful referral to one of our advertisers</p>
    <div class="offer__rule offer__rule--bottom"></div>
    <a class="offer__button" href="#">Learn More</a>
  </section>

  <section class="offer offer--two">
    <div class="offer__head">
      <svg width="244" height="139" viewBox="0 0 244 139">
        <defs>
          <linearGradient id="headLime" x1="0" y1="0" x2="0" y2="1">
            <stop offset="0" stop-color="#86c21c"/><stop offset="1" stop-color="#9fd02f"/>
          </linearGradient>
        </defs>
        <rect width="244" height="139" fill="url(#headLime)"/>
        <path d="M0 139 C30 40 130 -10 244 10 L244 139 Z" fill="#ffffff" opacity="0.1"/>
      </svg>
      <span class="offer__label">Offer</span>
      <span class="offer__number">2</span>
    </div>
    <h3 class="offer__title">Sign up a new business to offer referral commisions to ambassaadors</h3>
    <div class="offer__rule offer__rule--top"></div>
    <p class="offer__text">Earn up to <span class="offer__amount">$5000</span> or more when you earn 5% of money paid out by business in referral fees</p>
    <div class="offer__rule offer__rule--bottom"></div>
    <a class="offer__button" href="#">Learn More</a>
  </section>

  <section class="offer offer--three">
    <div class="offer__head">
      <svg width="244" height="139" viewBox="0 0 244 139">
        <rect width="244" height="139" fill="url(#headGreen)"/>
        <path d="M0 139 C30 40 130 -10 244 10 L244 139 Z" fill="#ffffff" opacity="0.08"/>
      </svg>
      <span class="offer__label">Offer</span>
      <span class="offer__number">3</span>
    </div>
    <h3 class="offer__title">Sign up new ambassadors</h3>
    <div class="offer__rule offer__rule--top"></div>
    <p class="offer__text">Earn up to <span class="offer__amount">$5000</span> or more when you earn 5% of the money the ambassadors you sign up earn</p>
    <div class="offer__rule offer__rule--bottom"></div>
    <a class="offer__button" href="#">Learn More</a>
  </section>

  <div class="payout-band">
    <span class="payout-band__label">Tarnwick Hub has paid over</span>
    <span class="payout-band__amount">$359,465 YTD</span>
  </div>

  <footer class="signup-band">
    <p class="signup-band__text">TarnwickHub, Fastest Growing Referral Marketplace. Earn income just by referring people you know.</p>
    <a class="signup-band__button" href="#">
      <svg width="20" height="20" viewBox="0 0 20 20" fill="none" stroke="#fff" stroke-width="1.6" stroke-linejoin="round">
        <rect x="1.5" y="9" width="4" height="9"/>
        <path d="M5.5 10 L9 3 C10.5 3 11 4 11 5.5 L10.5 8 L16.5 8 C17.8 8 18.6 9 18.3 10.3 L17 16.5 C16.8 17.5 16 18 15 18 L5.5 18"/>
      </svg>
      Free to Sign Up!
    </a>
  </footer>
</body>
</html>
```